Cafe / Bistro Website with a focus on Salads

I will be creating a wordpress site from the psds that you provide to me, i have attached a questionnaire and the answers to them to get an idea of what I'm looking for.

Reason: Id like to provide more time for designers to submit your designs, good luck!

Target Market(s)

20 - 45 years old downtown professionals

Industry/Entity Type

Cafe

Number of Pages Required

1 page

Requirements
Must have
• 1. Describe the products/services you sell.
• Cafe is open for breakfast and lunch serving fresh, made from scratch
• food and bakery items with an emphasis on their Fresh Bakery, Coffee,
• Panini & Deli Sandwiches, Fresh Salads with Homemade Dressings,
• Retail Items and Breakfast Items. (salads and dressings are their hottest
• selling items)
• 2. Age range of your target client base
• 20 - 45 years old
• Project-related questions
• 3. Technical skill level of your client base. Have a scale ranging from zero to ten with zero
• being the least technologically skilled and ten being the best.
• From 8 to 9 scale for tech savvy customers so mobile friendly is a must
• have.
Nice to have
• 4. Will your visitors require any special needs? Mobile version of site, multiple language
• support, larger type for easier reading, etc.)
• Just need the mobile friendly version as well.
• 5. Imagine your website in 5 years from now. Complete the sentence: I know my website works
• because…
• I know my website works because we have seen an increase in steady
• business and we are seeing new customers because of our online
• presence.
• 6. Name 3 things that are most important about the design of your new website.
• Branding matches our store look and feel, website has a clean look and
• its easy to read/user friendly.
• 7. Name 3 things that is least important in the design of your new website.
• 12. We don't need very much content, just enough to get them interested
• in visiting our store.
• 8. Do you have any color preferences, existing brand colors, and/or colors you do/not wish to
• include?
• Yes, we have uploaded a few interior pics not to be used on the site, but
• mainly for color and wood texture examples. Do your best to match the
• wood grain textures and the colors. A fun coffee cup similar to ours
• would be cool if its easy to create in Illustrator or Photoshop.
• 9. What are some existing websites that appeal to you? Provide links if possible.
• Not sure what sites I like that fit our store look and feel, sorry ;(
• © All Rights Reserved by Parlow Stackwise Labs 3
• Additional questions
• 10. Is your logo and other imagery web ready?
• 11. Do you have all images that you would like to be included in your website or would you like
• the designer to use imagery where appropriate?
• We can use stock photography where they see appropriate. I would like
• to use my food photos and merchandise photos, but maybe those are not
• seen on the home page? We can adjust once we see the first draft of the
• website designs.
• 12. Any specific features you would like included? Log in ability, calendars, forums, blog,
• subscription services (RSS, email or newsletters)?
• The only feature I could see using would be a calendar with days listing
• my type of soups and daily specials available. I should be able to know
• what those items are the last week of the month for the upcoming month.
• That would be cool and force me to be more organized with thinking
• ahead of time.
• PICKS RELATED AND MENTIONED ABOVE CAN ALL BE
• FOUND HERE…
• https://www.filtrovane.com/sh/kkbrupqtzlhwame/QQRmTE4bHuYpLosdwiKFMmpBe?dl=0

```html
<!DOCTYPE html>
<html lang="en">
<head>
<meta charset="utf-8">
<title>linden cafe</title>
<link rel="stylesheet" href="https://fonts.googleapis.com/css2?family=Oswald:wght@300;400;500&family=Open+Sans:wght@400;600;700&family=Roboto+Condensed:wght@400;700&display=swap">
<style>
:root{
  --wood:#3b3b3b;--wood-dark:#2c2c2c;--page:#ffffff;--ink:#333333;--muted:#555555;
  --brick:#8e1b17;--brick-dark:#6a120f;--leaf:#5f8a14;--leaf-text:#6c9a1d;
  --orange:#e8690f;--card:#e5e5e5;--card-line:#d2d2d2;--paper:#dedede;--footer:#e7e7e7;--black:#1e1e1e;
}
*{box-sizing:border-box;margin:0;padding:0}
html,body{width:709px;height:1200px;overflow:hidden}
body{position:relative;font-family:"Open Sans",sans-serif;color:var(--ink);
  background:repeating-linear-gradient(90deg,var(--wood) 0 7px,var(--wood-dark) 7px 9px,#434343 9px 15px,var(--wood) 15px 22px)}
.abs{position:absolute}
.page{position:absolute;left:36px;top:12px;width:637px;height:1176px;background:var(--page)}
.brand{left:46px;top:44px;display:flex;align-items:center;gap:6px;font-family:"Oswald",sans-serif;font-weight:500;font-size:20px;color:var(--brick-dark)}
.brand i{width:14px;height:14px;background:var(--brick-dark);display:block}
.login{left:626px;top:20px;width:38px;height:12px;border-radius:6px;background:var(--black);color:#fff;font:700 7px/12px "Open Sans",sans-serif;text-align:center}
.phone{right:45px;top:50px;font:400 17px/20px "Roboto Condensed",sans-serif;letter-spacing:1px;color:var(--leaf);display:flex;gap:6px;align-items:center}
.nav{left:174px;top:80px;width:490px;height:21px;background:var(--brick);border-top:2px solid var(--brick-dark);border-bottom:2px solid var(--brick-dark);display:flex;justify-content:space-around;align-items:center;padding:0 10px;
  clip-path:polygon(0 0,100% 0,99% 50%,100% 100%,0 100%,1% 50%)}
.nav a{color:#fff;text-decoration:none;font:400 10.5px "Oswald",sans-serif;letter-spacing:1.3px}
.hero{left:44px;top:114px;width:622px;height:274px;padding:7px;background:repeating-linear-gradient(45deg,#d8d8d8 0 2px,#fff 2px 5px)}
.hero-photo{width:100%;height:100%;background:linear-gradient(100deg,#e8ece9 0 30%,#c9453a 45%,#e06a35 60%,#6f8d3a 75%,#c83a30 90%)}
.hero-tag{left:85px;top:208px;width:180px;height:82px;background:var(--leaf);border:3px solid #84a93a;color:#fff;font:300 28px/29px "Oswald",sans-serif;padding:10px 0 0 8px;letter-spacing:.2px;white-space:nowrap}
.slide-arrow{top:238px;width:16px;height:26px;background:#444;display:flex;align-items:center;justify-content:center}
.card{top:400px;height:246px;background:var(--card);border:1px solid var(--card-line)}
.card p{font-size:8.9px;line-height:14.2px;color:var(--muted)}
.display{font-family:"Oswald",sans-serif;color:var(--black)}
.ph{background:linear-gradient(135deg,#c9a073,#e9dcc6)}
.events-title{left:0;width:709px;top:670px;text-align:center;font:400 19px "Oswald",sans-serif}
.date-bar{left:243px;top:708px;width:223px;height:14px;background:#e9e9e9;font-size:10px;line-height:14px;text-align:center}
.date-bar b{position:absolute;top:0;width:26px;height:14px;background:var(--orange);clip-path:polygon(20% 0,80% 0,100% 50%,80% 100%,20% 100%,0 50%)}
.week{left:89px;top:740px;width:531px;height:52px;display:flex;background:#e6e6e6;border-bottom:3px solid var(--orange)}
.day{flex:1;padding:5px 7px;border-right:1px solid #fff}
.day small{display:block;font-size:6.5px;font-weight:700;color:#999}
.day strong{display:block;font:700 11.5px/15px "Open Sans",sans-serif;color:#555}
.day span{display:block;font-size:8px;color:var(--orange)}
.day.active{background:var(--orange)}
.day.active *{color:#fff}
.event-list{left:89px;top:793px;width:531px;height:79px;background:#ececec}
.event{position:absolute;top:11px;display:flex;gap:10px}
.event .ph{width:58px;height:58px;background:linear-gradient(135deg,#d3a46b,#f2ede5)}
.event h4{font-size:9.5px;margin-bottom:6px}
.event p{font-size:8px;line-height:13px;color:#555}
.visit{top:900px;width:193px;height:100px;background:var(--paper);text-align:center;padding-top:16px}
.visit small{display:block;font:400 10px "Oswald",sans-serif;color:#333}
.visit strong{display:block;font:400 16px/16px "Oswald",sans-serif;color:#222}
.corner{position:absolute;width:8px;height:8px;background:var(--black)}
.footer{left:36px;top:1032px;width:637px;height:156px;background:var(--footer)}
.hang{position:absolute;top:1052px;width:92px;height:11px;background:var(--black);color:#fff;font:700 8px/11px "Open Sans",sans-serif;text-align:center;clip-path:polygon(0 0,100% 0,96% 50%,100% 100%,0 100%,4% 50%)}
.foot-text{position:absolute;top:1078px;font-size:8.5px;line-height:13.5px;text-align:center;color:#444}
.email{left:470px;top:1108px;width:150px;height:24px;border:1px solid #aaa;background:#fff;font-size:8.5px;line-height:22px;padding-left:7px;color:#666}
.go{left:626px;top:1108px;width:38px;height:24px;border:1px solid #aaa;background:#f3f3f3;font:400 10px/22px "Oswald",sans-serif;text-align:center}
.social{left:305px;top:1150px;display:flex;gap:5px}
.social i{width:15px;height:15px;border-radius:50%;background:#888;display:block}
.rule{position:absolute;top:1157px;height:3px;background:#999}
.legal{position:absolute;top:1171px;font-size:8.5px;color:#444;white-space:nowrap}
.legal-links{right:45px;display:flex;gap:10px}
</style>
</head>
<body>
<div class="page"></div>

<div class="abs brand"><i></i>linden cafe</div>
<div class="abs login">LOGIN</div>
<div class="abs phone">
  <svg width="14" height="12" viewBox="0 0 14 12"><path d="M1 4c0-3 12-3 12 0l-3 1-1-2H5L4 5z" fill="#555"/><rect x="3" y="6" width="8" height="5" rx="1" fill="#555"/></svg>
  555. 014. 2290
</div>
<nav class="abs nav">
  <a>HOME</a><a>ABOUT</a><a>MENU</a><a>CALENDER</a><a>GALLERY</a><a>CONTACTS</a><a>BLOG</a>
</nav>

<div class="abs hero"><div class="hero-photo" role="img" aria-label="Fresh tomato and arugula salad with feta on a white plate"></div></div>
<div class="abs hero-tag">I MAKE GREAT<br>FOOD &amp; COFFEE</div>
<div class="abs slide-arrow" style="left:35px"><svg width="6" height="10"><path d="M5 0 0 5l5 5" stroke="#fff" fill="none"/></svg></div>
<div class="abs slide-arrow" style="left:658px"><svg width="6" height="10"><path d="M1 0l5 5-5 5" stroke="#fff" fill="none"/></svg></div>

<section class="abs card" style="left:44px;width:197px">
  <div class="abs" style="left:132px;top:8px;width:40px;height:46px;background:#d4d4d4" role="img" aria-label="Steaming coffee cup sketch"></div>
  <div class="abs display" style="left:10px;top:26px;font-size:11px;line-height:12px">Welcome to<br><span style="font-size:20px;line-height:24px">linden cafe</span></div>
  <p class="abs" style="left:10px;top:79px;width:182px">Lorem ipsum dolor sit amet, consectetur adipiscing elit, sed do eiusmod tempor incididunt ut labore et dolore magna aliqua. Ut enim ad minim veniam, quis nostrud exercitation ullamco laboris nisi ut aliquip ex ea commodo consequat. Duis aute irure dolor in reprehenderit in voluptate velit esse cillum dolore eu fugiat nulla pariatur. Excepteur sint occaecat cupidatat non proident, sunt in culpa qui.</p>
</section>

<section class="abs card" style="left:257px;width:196px">
  <div class="abs" style="left:15px;top:28px;width:164px;height:12px;background:#d2d2d2"></div>
  <div class="abs display" style="left:0;width:196px;top:22px;text-align:center;font-size:16px"><span style="background:var(--card);padding:0 6px">Best offer</span></div>
  <div class="abs" style="left:0;width:196px;top:52px;text-align:center;font:400 14px 'Roboto Condensed',sans-serif;color:var(--leaf-text)">Breakfast&nbsp; 07:00 - 10:00</div>
  <div class="abs ph" style="left:10px;top:83px;width:174px;height:150px" role="img" aria-label="Coffee and croissant breakfast on a wooden table"></div>
  <div class="abs" style="left:20px;top:197px;width:34px;height:40px;background:var(--orange);clip-path:polygon(0 0,100% 0,100% 80%,50% 100%,0 80%);color:#fff;text-align:center;font:400 15px/14px 'Oswald',sans-serif;padding-top:14px">$5</div>
  <div class="abs" style="left:17px;top:197px;width:40px;height:10px;background:var(--leaf);color:#fff;font:700 6px/10px 'Open Sans',sans-serif;text-align:center">ONLY FOR</div>
</section>

<section class="abs card" style="left:469px;width:197px">
  <div class="abs display" style="left:0;width:197px;top:20px;text-align:center;font-size:10px;line-height:11px">The last week of the month for<br><span style="font-size:16px;line-height:18px">the upcoming month</span></div>
  <div class="abs" style="left:11px;top:61px;width:175px;height:110px;background:linear-gradient(135deg,#f2e7cf,#d9a25a,#f6f1e6)" role="img" aria-label="Grilled wrap with pasta on a plate"></div>
  <div class="abs" style="left:11px;top:179px;font-size:9px;font-weight:700">Dish name here</div>
  <p class="abs" style="left:11px;top:191px;width:178px;font-size:8.9px;line-height:13px">Lorem ipsum dolor sit amet, consectetur adipiscing elit, sed do eiusmod tempor incididunt ut labore et</p>
</section>

<h2 class="abs events-title">Weekly events</h2>
<div class="abs date-bar">
  <b style="left:0"></b>April 19, 2015 ~ April 25, 2015<b style="right:0"></b>
</div>
<div class="abs week">
  <div class="day"><small>APRIL 19</small><strong>Sun</strong><span>2 EVENT</span></div>
  <div class="day"><small>APRIL 19</small><strong>Mon</strong><span>1 EVENT</span></div>
  <div class="day active"><small>APRIL 19</small><strong>Tue</strong><span>2 EVENT</span></div>
  <div class="day"><small>APRIL 19</small><strong>Wed</strong><span style="color:#999">0 EVENT</span></div>
  <div class="day"><small>APRIL 19</small><strong>Thu</strong><span>2 EVENT</span></div>
  <div class="day"><small>APRIL 19</small><strong>Fri</strong><span>2 EVENT</span></div>
  <div class="day" style="border:0"><small>APRIL 19</small><strong>Sat</strong><span>1 EVENT</span></div>
</div>
<div class="abs event-list">
  <div class="event" style="left:10px"><div class="ph" role="img" aria-label="Coffee cup with pastry"></div><div><h4>Lorem ipsum dolor</h4><p>7:00 pm - 9:00 pm<br>Lorem ipsum dolor sit amet, consectetur<br>adipiscing elit, sed do</p></div></div>
  <div class="event" style="left:273px"><div class="ph" role="img" aria-label="Coffee served in a cafe interior"></div><div><h4>Lorem ipsum dolor</h4><p>7:00 pm - 9:00 pm<br>Lorem ipsum dolor sit amet, consectetur<br>adipiscing elit, sed do</p></div></div>
</div>

<a class="abs visit" style="left:46px">
  <small>Visit</small><strong>BLOG</strong>
  <svg width="24" height="22" viewBox="0 0 24 22" style="margin-top:4px"><path d="M12 1C5 1 1 5 1 9s3 7 7 8l-3 4 7-4c6 0 11-3 11-8S19 1 12 1z" fill="#222"/><path d="M8 12l6-6 2 2-6 6H8z" fill="#fff"/></svg>
  <i class="corner" style="left:0;top:0;clip-path:polygon(0 0,100% 0,0 100%)"></i><i class="corner" style="right:0;top:0;clip-path:polygon(0 0,100% 0,100% 100%)"></i><i class="corner" style="left:0;bottom:0;clip-path:polygon(0 0,0 100%,100% 100%)"></i><i class="corner" style="right:0;bottom:0;clip-path:polygon(100% 0,100% 100%,0 100%)"></i>
</a>
<a class="abs visit" style="left:259px">
  <small>Read</small><strong>MENU</strong>
  <svg width="24" height="22" viewBox="0 0 24 22" style="margin-top:4px"><path d="M1 2l11 3 11-3v18l-11 2-11-2z" fill="#222"/><path d="M8 6v10M7 6v4h2V6M15 6c2 0 2 5 0 5v5" stroke="#fff" stroke-width="1.3" fill="none"/></svg>
  <i class="corner" style="left:0;top:0;clip-path:polygon(0 0,100% 0,0 100%)"></i><i class="corner" style="right:0;top:0;clip-path:polygon(0 0,100% 0,100% 100%)"></i><i class="corner" style="left:0;bottom:0;clip-path:polygon(0 0,0 100%,100% 100%)"></i><i class="corner" style="right:0;bottom:0;clip-path:polygon(100% 0,100% 100%,0 100%)"></i>
</a>
<a class="abs visit" style="left:471px">
  <small>Visit</small><strong>FORUMS</strong>
  <svg width="24" height="22" viewBox="0 0 24 22" style="margin-top:4px"><circle cx="7" cy="5" r="3" fill="#222"/><circle cx="16" cy="5" r="3" fill="#222"/><path d="M2 20v-7c0-3 10-3 10 0v7zM11 20v-7c0-3 10-3 10 0v7z" fill="#222"/><circle cx="18" cy="16" r="4" fill="#222" stroke="#dedede"/></svg>
  <i class="corner" style="left:0;top:0;clip-path:polygon(0 0,100% 0,0 100%)"></i><i class="corner" style="right:0;top:0;clip-path:polygon(0 0,100% 0,100% 100%)"></i><i class="corner" style="left:0;bottom:0;clip-path:polygon(0 0,0 100%,100% 100%)"></i><i class="corner" style="right:0;bottom:0;clip-path:polygon(100% 0,100% 100%,0 100%)"></i>
</a>

<footer class="abs footer"></footer>
<svg class="abs" style="left:0;top:1034px" width="709" height="20">
  <g stroke="#222" fill="none"><path d="M126 18l16-14 16 14M339 18l16-14 16 14M552 18l16-14 16 14"/></g>
</svg>
<div class="hang" style="left:96px">VISIT US</div>
<div class="hang" style="left:309px">OUR HOURS</div>
<div class="hang" style="left:522px">GET THE LATEST</div>
<address class="foot-text" style="left:62px;width:160px;font-style:normal">418, 5th ave.N<br>Riverton,mn<br>55990<br>555. 014. 2290<br>info@lindencafe.com</address>
<p class="foot-text" style="left:275px;width:160px">Open Monday to friday<br>6:00am - 3:30pm<br>Saturday to Sunday<br>Holidays</p>
<p class="foot-text" style="left:470px;width:194px">Want to keep abreast of the latest happenings at the Café? Then sign up today!</p>
<div class="abs email">E-mail address</div>
<div class="abs go">GO</div>
<div class="rule" style="left:44px;width:212px;background:#bbb;height:1px;top:1158px"></div>
<div class="rule" style="left:256px;width:46px"></div>
<div class="abs social"><i></i><i></i><i></i><i></i><i></i></div>
<div class="rule" style="left:408px;width:46px"></div>
<div class="rule" style="left:454px;width:210px;background:#bbb;height:1px;top:1158px"></div>
<div class="legal" style="left:44px">© 2015 linden cafe . All right reserved</div>
<div class="legal legal-links"><span>Term of Use</span><span>Privacy Policy</span><span>Contact</span></div>
</body>
</html>
```